Instructions for nurses on how to give a report on each shift

I have a 2-page reference sheet that needs to be updated to look more aesthetically pleasing.

Target Market(s)

Healthcare, nurses

Industry/Entity Type

Healthcare

Font styles to use
Sans Serif

Requirements
Must have
• Please make sure it is easy to read, the content is well organized and has a flow to it. Please also pick colors that would coordinate with our website www.brivolen.org (so mainly navy and white or off-white with accent colors.) Please make sure to add accent colors to break up the content. The MORVY name and title at the top should remain on the page but I'm not married to the star or logo style. You can do what you think looks best there. Way at the bottom in fine print, I would like for you to add BRIVOLEN © 2019 All rights reserved.

```html
<!DOCTYPE html>
<html lang="en">
<head>
<meta charset="utf-8">
<title>MORVY Shift Report Reference Sheet</title>
<link rel="stylesheet" href="https://fonts.googleapis.com/css2?family=Source+Sans+3:wght@400;600;700&display=swap">
<style>
  :root {
    --canvas: #c6e4f6;
    --navy: #0b3a63;
    --ink: #1b2f4a;
    --sky: #c8e3f5;
    --mist: #e4e6e9;
    --white: #ffffff;
    --line: #dbe8f2;
    --brand: #2f6aa8;
  }
  * { box-sizing: border-box; margin: 0; padding: 0; }
  html, body { width: 966px; height: 1200px; overflow: hidden; }
  body {
    background: var(--canvas);
    font-family: "Source Sans 3", Arial, sans-serif;
    color: var(--ink);
    position: relative;
  }
  .sheet { position: absolute; background: var(--navy); overflow: hidden; }
  .sheet--chart { left: 98px; top: 40px; width: 766px; height: 540px; }
  .sheet--guide { left: 97px; top: 606px; width: 773px; height: 546px; }
  .sheet__art { position: absolute; inset: 0; }
  .brand { position: absolute; left: 42px; top: 30px; }
  .brand__name {
    display: flex; align-items: center; gap: 6px;
    font-size: 22px; font-weight: 600; color: var(--brand); letter-spacing: 1px; line-height: 1;
  }
  .brand__mark { width: 14px; height: 14px; background: var(--brand); }
  .brand__tagline {
    margin-top: 5px; width: 170px;
    font-size: 9px; line-height: 10px; font-weight: 600; color: var(--brand);
  }
  .footer {
    position: absolute; left: 0; right: 0; text-align: center;
    color: var(--white); font-weight: 700; font-size: 11px; line-height: 1;
  }
  .sheet--chart .footer { top: 516px; }
  .sheet--guide .footer { top: 521px; }
  .footer span { background: var(--navy); padding: 0 8px; }

  .leader { position: absolute; left: 231px; top: 122px; width: 296px; height: 72px; background: var(--sky); border: 1px solid var(--white); }
  .leader__title { background: var(--white); border-bottom: 2px solid var(--navy); height: 19px; text-align: center; font-weight: 700; font-size: 12px; line-height: 18px; color: var(--navy); }
  .leader__fields { padding: 7px 0 0 24px; font-size: 10px; line-height: 12px; font-weight: 600; }

  .questions, .answers {
    position: absolute; left: 41px; width: 686px;
    display: grid; grid-template-columns: repeat(5, 125px); column-gap: 15.25px;
  }
  .questions { top: 232px; }
  .answers { top: 381px; }
  .question { height: 116px; background: var(--sky); border-radius: 7px; padding: 8px 7px 0 7px; }
  .question__ask { font-size: 10px; font-weight: 700; line-height: 11.5px; }
  .question__list { margin-top: 9px; list-style: none; font-size: 9px; line-height: 11.5px; }
  .question__list--two { display: grid; grid-template-columns: 62px auto; }
  .question__list--two .full { grid-column: 1 / -1; }
  .question__list li::before { content: "• "; }
  .question__list li.gap::before { content: ""; }
  .answer-pair { display: flex; gap: 11px; }
  .answer { height: 117px; background: var(--mist); border-radius: 7px; text-align: center; padding: 10px 3px 0; font-size: 7.6px; line-height: 9.6px; }
  .answer--no { width: 56px; }
  .answer--yes { width: 58px; }
  .answer__label { font-weight: 700; font-size: 9.5px; margin-bottom: 9px; }
  .answer__blanks { text-align: left; padding-left: 3px; }

  .motto { position: absolute; left: 0; right: 0; top: 144px; text-align: center; color: var(--white); font-weight: 700; font-size: 22px; }
  .guide-col { position: absolute; top: 214px; }
  .guide-col--left { left: 50px; width: 300px; }
  .guide-col--right { left: 376px; width: 310px; }
  .topic__head { background: var(--sky); color: var(--navy); font-weight: 700; font-size: 11px; line-height: 18px; height: 18px; padding-left: 8px; }
  .guide-col--left .topic__head { width: 253px; }
  .topic__list { color: var(--white); font-size: 8.6px; line-height: 10.5px; padding: 10px 0 9px 40px; }
  .topic__list li { padding-left: 6px; }
  .guide-col--right .topic__list { padding: 10px 0 9px 46px; }
</style>
</head>
<body>

<section class="sheet sheet--chart" aria-label="Shift report flow chart">
  <svg class="sheet__art" width="766" height="540" viewBox="0 0 766 540" aria-hidden="true">
    <polygon points="0,22 766,22 766,66 298,66 210,98 0,98" fill="#ffffff"/>
    <polyline points="22,98 22,522 744,522 744,66" fill="none" stroke="#dbe8f2" stroke-width="1"/>
    <g stroke="#dbe8f2" stroke-width="1" fill="none">
      <line x1="380" y1="194" x2="380" y2="210"/>
      <line x1="98" y1="210" x2="663" y2="210"/>
      <line x1="98" y1="210" x2="98" y2="232"/>
      <line x1="242" y1="210" x2="242" y2="232"/>
      <line x1="380" y1="210" x2="380" y2="232"/>
      <line x1="522" y1="210" x2="522" y2="232"/>
      <line x1="663" y1="210" x2="663" y2="232"/>
      <path d="M103 348 V366 M67 366 H138 M67 366 V381 M138 366 V381"/>
      <path d="M243 348 V366 M207 366 H278 M207 366 V381 M278 366 V381"/>
      <path d="M384 348 V366 M348 366 H419 M348 366 V381 M419 366 V381"/>
      <path d="M524 348 V366 M488 366 H559 M488 366 V381 M559 366 V381"/>
      <path d="M665 348 V366 M629 366 H700 M629 366 V381 M700 366 V381"/>
    </g>
  </svg>

  <div class="brand">
    <div class="brand__name"><span class="brand__mark"></span>MORVY</div>
    <p class="brand__tagline">Shift Report Reference Guide for Nursing Teams</p>
  </div>

  <div class="leader">
    <div class="leader__title">LEADER</div>
    <div class="leader__fields">Name:<br>Title:<br>Assignment:</div>
  </div>

  <div class="questions">
    <div class="question">
      <p class="question__ask">Any change in resident status?</p>
      <ul class="question__list"><li>Admissions</li><li>Discharges</li><li>Transfers</li><li>Appointments</li></ul>
    </div>
    <div class="question">
      <p class="question__ask">Any concerning changes in resident’s condition?</p>
      <ul class="question__list question__list--two"><li>Pain</li><li>Skin</li><li>Ambulation</li><li>Safety</li><li>Behavior</li><li class="gap"></li><li>Appetite</li><li>Elimination</li></ul>
    </div>
    <div class="question">
      <p class="question__ask">Any residents requiring extraordinary monitoring?</p>
      <ul class="question__list"><li>Falls</li><li>Decline in condition</li><li>IV/ABT therapy</li><li>Hospice</li></ul>
    </div>
    <div class="question">
      <p class="question__ask">Any concerns related to residents environment?</p>
      <ul class="question__list"><li>Room temperature</li><li>Supplies</li><li>Equipment</li></ul>
    </div>
    <div class="question">
      <p class="question__ask">Any concerns or barriers related to your ability to perform your job effectively?</p>
      <ul class="question__list question__list--two" style="margin-top:5px"><li>Supplies</li><li>Acuity</li><li class="full">Time constraints</li><li class="full">Family requests</li><li class="full">Environment</li></ul>
    </div>
  </div>

  <div class="answers">
    <div class="answer-pair">
      <div class="answer answer--no"><p class="answer__label">NO</p><p>“I do not have any actual or expected changes in resident status.”</p></div>
      <div class="answer answer--yes"><p class="answer__label">YES</p><p>“My residents with changes in their status are…”</p><p class="answer__blanks"><br>1)________<br>2)________<br>3)________</p></div>
    </div>
    <div class="answer-pair">
      <div class="answer answer--no"><p class="answer__label">NO</p><p>“I have no residents with concerning changes in their condition.”</p></div>
      <div class="answer answer--yes"><p class="answer__label">YES</p><p>“My residents w/ concerning changes in their condition include…”</p><p class="answer__blanks">1)________<br>2)________<br>3)________</p></div>
    </div>
    <div class="answer-pair">
      <div class="answer answer--no"><p class="answer__label">NO</p><p>“I have no residents requiring extraordi-nary monitor-ing.”</p></div>
      <div class="answer answer--yes"><p class="answer__label">YES</p><p>“My residents that require extraordinary monitoring are…”</p><p class="answer__blanks">1)________<br>2)________<br>3)________</p></div>
    </div>
    <div class="answer-pair">
      <div class="answer answer--no"><p class="answer__label">NO</p><p>“I have no concerns related to my residents environment.”</p></div>
      <div class="answer answer--yes"><p class="answer__label">YES</p><p>“My residents with concerns related to their environment include…”</p><p class="answer__blanks">1)________<br>2)________<br>3)________</p></div>
    </div>
    <div class="answer-pair">
      <div class="answer answer--no"><p class="answer__label">NO</p><p>“I have no concerns or barriers affecting my ability to perform my job.”</p></div>
      <div class="answer answer--yes"><p class="answer__label">YES</p><p>“My concerns affecting my ability to perform my job include…”</p><p class="answer__blanks">1)________<br>2)________<br>3)________</p></div>
    </div>
  </div>

  <p class="footer"><span>BRIVOLEN © 2019 All rights reserved.</span></p>
</section>

<section class="sheet sheet--guide" aria-label="Shift report meeting guide">
  <svg class="sheet__art" width="773" height="546" viewBox="0 0 773 546" aria-hidden="true">
    <polygon points="0,24 773,24 773,66 302,66 212,100 0,100" fill="#ffffff"/>
    <polyline points="22,100 22,527 753,527 753,66" fill="none" stroke="#dbe8f2" stroke-width="1"/>
  </svg>

  <div class="brand" style="top:32px">
    <div class="brand__name"><span class="brand__mark"></span>MORVY</div>
    <p class="brand__tagline">Shift Report Reference Guide for Nursing Teams</p>
  </div>

  <h1 class="motto">When “I” is replaced by “WE” Even illness becomes wellness.</h1>

  <div class="guide-col guide-col--left">
    <div class="topic">
      <h2 class="topic__head">OBJECTIVES</h2>
      <ul class="topic__list">
        <li>Accountability: Declare roles and assignments</li>
        <li>Advocacy: Identify patient needs</li>
        <li>Critical Thinking: Prioritize and recognize obstacles</li>
        <li>Communication: Share important information</li>
        <li>Collaboration: Utilize an interdisciplinary approach</li>
      </ul>
    </div>
    <div class="topic">
      <h2 class="topic__head">OUTCOMES:</h2>
      <ul class="topic__list">
        <li>Share best practices</li>
        <li>Improve communication</li>
        <li>Promote cohesiveness</li>
        <li>Increase staff morale</li>
        <li>Enhance patient and organizational outcomes</li>
      </ul>
    </div>
    <div class="topic">
      <h2 class="topic__head">WHO:</h2>
      <ul class="topic__list">
        <li>All nurses on the unit</li>
        <li>All nursing support staff (CNA/MA/HCT)</li>
        <li>Administrator</li>
        <li>Director of Nursing</li>
        <li>Head of pertinent disciplines (Dietary, Social Work, Physical Therapy, Engineering, Central Supply, etc.)</li>
      </ul>
    </div>
  </div>

  <div class="guide-col guide-col--right">
    <div class="topic">
      <h2 class="topic__head">WHEN:</h2>
      <ul class="topic__list">
        <li>Every morning (assign a meeting time for each unit )</li>
        <li>Keep meetings within 15 minutes in length</li>
      </ul>
    </div>
    <div class="topic">
      <h2 class="topic__head">WHERE:</h2>
      <ul class="topic__list">
        <li>Nursing station on each unit</li>
      </ul>
    </div>
    <div class="topic">
      <h2 class="topic__head">HELPFUL TIPS:</h2>
      <ul class="topic__list">
        <li>Assign a meeting facilitator (usually the administrator of the facility)</li>
        <li>Standing during meetings keeps the meetings short and to the point</li>
        <li>Keeping meetings within 15 minutes emphasizes being prepared and direct</li>
        <li>Keep meeting times consistent (morning is best)</li>
        <li>Do not begin until everyone is present (minimizes stragglers)</li>
        <li>Avoid discussing personal concerns</li>
        <li>Include reminders for in-services, meetings, etc. and updates towards the end of the meeting</li>
        <li>Always conclude with achievements, milestones, praise, words of encouragement, motivational quote, etc.</li>
      </ul>
    </div>
  </div>

  <p class="footer"><span>BRIVOLEN © 2019 All rights reserved.</span></p>
</section>

</body>
</html>
```